Improvement of design for elearning template

Our company provides web based elearning courses for employees. We have a design layout for the different slides which can be found here: https://www.filecrate-share.example/s/qk7tr2mplx9e/BXnTpWvZrKdMeYfLs4QjHcUa?view=1. The content will be added later. At this point we are just looking for a design layout that works with different content types like images, text, quiz & videos. What we would ask you, is to pick randomly 1 or 2 of the elearning slides from the existing designs and suggest improvements or come up with an alternative design. The winner of the design project can work on all slides and this will be a project with a much larger budget.
Target Market(s)
Employees in large enterprises
Look and feel
Each slider illustrates characteristics of the customer's brand and the style your logo design should communicate.

```html
<!DOCTYPE html>
<html lang="en">
<head>
<meta charset="utf-8">
<title>eLearning slide layouts</title>
<link rel="stylesheet" href="https://fonts.googleapis.com/css2?family=Figtree:wght@400;500;600;700;800&display=swap">
<style>
:root{
  --board:#868686;
  --paper:#ffffff;
  --header:#fafafb;
  --rule:#e6e8ee;
  --brand:#0b2fa0;
  --brand-deep:#0a2a8f;
  --ink:#1b1d26;
  --muted:#6b6f7a;
  --track:#e7e8ec;
  --go:#5cc443;
  --tile:#f3f3f5;
  --tile-line:#d9dadf;
  --art-a:#dbe6fb;
  --art-b:#7f9ef0;
  --art-c:#2747b8;
}
*{box-sizing:border-box;margin:0;padding:0}
html,body{width:1200px;height:654px;overflow:hidden;background:var(--board)}
body{font-family:"Figtree",sans-serif;color:var(--ink);position:relative}
.slide{position:absolute;width:543px;height:279px;background:var(--paper);overflow:hidden}
.slide--welcome{left:41px;top:34px}
.slide--lesson{left:615px;top:34px}
.slide--exam{left:41px;top:342px}
.slide--gallery{left:615px;top:342px}

.topbar{position:absolute;left:0;top:0;width:100%;height:36px;background:var(--header);border-bottom:1px solid var(--rule)}
.brand{position:absolute;left:52px;top:13px;display:flex;align-items:center;gap:5px;color:var(--brand);font-size:8.4px}
.brand__mark{width:11px;height:11px;border:1.2px solid var(--brand);border-radius:50%}
.nav{position:absolute;right:63px;top:13px;display:flex;gap:14px;font-size:8.4px;color:var(--ink)}
.nav span::before{content:"";display:inline-block;width:4px;height:4px;border-right:1px solid var(--ink);border-bottom:1px solid var(--ink);transform:rotate(45deg) translate(-2px,-1px);margin-right:5px}

.art{position:absolute;border-radius:40px 60px 30px 70px}
.art--team{left:292px;top:40px;width:240px;height:225px;background:radial-gradient(ellipse at 50% 55%,var(--art-b) 0%,var(--art-a) 55%,rgba(255,255,255,0) 75%)}
.art--device{left:340px;top:57px;width:172px;height:191px;background:linear-gradient(160deg,var(--art-a),var(--art-b) 55%,var(--art-c))}

.welcome__kicker{position:absolute;left:71px;top:90px;font-size:11px}
.welcome__title{position:absolute;left:70px;top:106px;font-size:19px;line-height:22px;font-weight:800;color:var(--brand)}
.facts{position:absolute;left:70px;top:161px;display:flex;gap:14px;font-size:7px}
.facts dt{color:var(--ink)}
.facts dd{font-weight:700;font-size:7.8px;margin-top:2px}
.btn-start{position:absolute;left:71px;top:204px;width:66px;height:20px;border-radius:10px;background:var(--brand);color:#fff;font-size:10px;display:flex;align-items:center;justify-content:center}
.credits{position:absolute;left:9px;top:267px;font-size:4px}

.kicker{position:absolute;left:51px;top:54px;font-size:10px;color:var(--brand)}
.headline{position:absolute;left:51px;top:67px;font-size:13px;font-weight:800;color:var(--brand)}
.headline::after{content:"";position:absolute;left:0;top:20px;width:55px;height:1px;background:var(--brand)}
.body{position:absolute;left:51px;top:106px;width:265px;font-size:7px;line-height:8.9px}
.body p{margin-bottom:8.5px}
.body .bullet{padding-left:4px;text-indent:-4px}

.progress{position:absolute;left:20px;top:247px;width:505px;height:20px;font-size:7px}
.progress__pct{position:absolute;left:42px;top:0;font-size:6px}
.progress__track{position:absolute;left:0;top:12px;width:376px;height:2.5px;border-radius:2px;background:var(--track)}
.progress__fill{position:absolute;left:0;top:0;width:48px;height:100%;border-radius:2px;background:var(--go)}
.progress__lesson{position:absolute;left:379px;top:8px}
.progress__prev{position:absolute;left:432px;top:8px;display:flex;align-items:center;gap:3px}
.progress__next{position:absolute;left:472px;top:8px;display:flex;align-items:center;gap:3px}

.exam__title{position:absolute;left:51px;top:54px;font-size:10px;color:var(--brand)}
.exam__note{position:absolute;left:51px;top:79px;width:380px;font-size:5px;line-height:6.5px;color:var(--muted)}
.exam__tag{position:absolute;left:228px;top:105px;width:85px;height:13px;border:1px solid var(--rule);border-radius:7px;font-size:7px;display:flex;align-items:center;justify-content:center}
.exam__question{position:absolute;left:71px;top:126px;width:400px;text-align:center;font-size:11px;line-height:14px;font-weight:500}
.choices{position:absolute;left:92px;top:162px;width:355px;list-style:none}
.choices li{height:16px;margin-bottom:2.6px;border-radius:8px;background:#f7f7f8;display:flex;align-items:center;font-size:8.4px;padding-left:6px}
.choices li::before{content:"";width:8px;height:8px;border:1px solid var(--brand);border-radius:50%;margin-right:6px}
.exam__steps{position:absolute;left:225px;top:241px;font-size:5px;color:var(--brand);display:flex;align-items:center;gap:4px}
.dots{display:flex;gap:1.4px}
.dots i{width:2.2px;height:2.2px;border-radius:50%;background:#d2d4da}
.dots i.on{background:var(--brand)}

.grid{position:absolute;left:78px;top:109px}
.tile{position:absolute;width:83px}
.tile svg{display:block;width:83px;height:50px}
.tile span{display:block;text-align:center;font-size:6.5px;font-weight:600;margin-top:8px}
.tip{position:absolute;left:269px;top:130px;width:77px;height:61px;background:#fff;border-radius:5px;box-shadow:0 2px 8px rgba(0,0,0,.15);padding:9px 8px;font-size:6px;line-height:8.8px}
.tip::before{content:"";position:absolute;left:-7px;top:16px;border:6px solid transparent;border-right-color:#fff;border-top-color:#fff;transform:rotate(15deg)}
</style>
</head>
<body>

<section class="slide slide--welcome">
  <header class="topbar">
    <div class="brand"><i class="brand__mark"></i>Company name</div>
    <nav class="nav"><span>Lessons</span><span>Menu</span><span>Glossary</span></nav>
  </header>
  <div class="art art--team" role="img" aria-label="Illustration of two colleagues beside a padlock and shield, symbolising data protection"></div>
  <p class="welcome__kicker">Welcome to the course</p>
  <h1 class="welcome__title">Handling sensitive<br>information</h1>
  <dl class="facts">
    <div><dt>Duration</dt><dd>30 minutes</dd></div>
    <div><dt>Complexity</dt><dd>Medium</dd></div>
    <div><dt>Audience</dt><dd>All</dd></div>
    <div><dt>Interactive</dt><dd>Yes</dd></div>
  </dl>
  <div class="btn-start">Start</div>
  <p class="credits">Creation year: 2009 | Version 1.1</p>
</section>

<section class="slide slide--lesson">
  <header class="topbar">
    <div class="brand"><i class="brand__mark"></i>Company name</div>
    <nav class="nav"><span>Lessons</span><span>Menu</span><span>Glossary</span></nav>
  </header>
  <p class="kicker">Handling sensitive information</p>
  <h2 class="headline">Ad minim veniam, quis nostrud exerci tation</h2>
  <div class="body">
    <p>Lorem ipsum dolor sit amet, consectetuer adipiscing elit, sed diam nonummy nibh euismod tincidunt ut lacreet dolore magna aliquam erat volupat. Ut wisi enim ad minim veniam, quis nostrud exerci tation ullamcorp</p>
    <p class="bullet">- Er suscipit lobartis nis ut aliquip Duis autem vel eum iriure Vel illum dolore eu feugiat nulla facilisis at vero</p>
    <p class="bullet">- Er suscipit lobartis nis ut aliquip Duis autem vel eum iriure Vel illum dolore eu feugiat nulla facilisis at vero</p>
    <p>Praesent luptatum zzril delerit augue duis dolore te feugait dolore te feugait nulla facilisi. Lorem ipsum dolor sit amet, cons ectetuer adipiscing elit, sed diam nonummy nibh euismod tincidunt ut laoreet dolore magna aliquam erat volutpat. Ut wisi enim ad minim veniam, quis nostrud exerci tation</p>
  </div>
  <div class="art art--device" role="img" aria-label="Illustration of a person unlocking a large smartphone with a fingerprint, a shield and a bank card"></div>
  <div class="progress">
    <span class="progress__pct">10%</span>
    <div class="progress__track"><div class="progress__fill"></div></div>
    <span class="progress__lesson">Lesson 2</span>
    <span class="progress__prev"><svg width="11" height="7" viewBox="0 0 11 7"><path d="M10.5 3.5H1M4 .5L1 3.5 4 6.5" fill="none" stroke="#5cc443" stroke-width="1.2"/></svg>Prev.</span>
    <span class="progress__next">Next<svg width="11" height="7" viewBox="0 0 11 7"><path d="M.5 3.5H10M7 .5l3 3-3 3" fill="none" stroke="#5cc443" stroke-width="1.2"/></svg></span>
  </div>
</section>

<section class="slide slide--exam">
  <header class="topbar">
    <div class="brand"><i class="brand__mark"></i>Company name</div>
    <nav class="nav"><span>Lessons</span><span>Menu</span><span>Glossary</span></nav>
  </header>
  <h2 class="exam__title">Phishing awareness | Exam Questions</h2>
  <p class="exam__note">The exam contains 5 multiple choice questions. Please choose the correct answer. You are only allowed to give a maximum of 3 incorrect answers, otherwise the training starts all over again.</p>
  <div class="exam__tag">1. E-mail use</div>
  <p class="exam__question">If you receive an e-mail with the following subject line: "Congratulations, you have won a week's holiday for two people in Italy." What do you?</p>
  <ul class="choices">
    <li>You are curious and open the e-mail</li>
    <li>You check whether you know the sender. If not, delete the e-mail unread.</li>
    <li>You send the e-mail to the service desk</li>
    <li>You are happy about this and forward the e-mail to your partner and colleagues</li>
  </ul>
  <div class="exam__steps">Exam progress
    <span class="dots"><i class="on"></i><i class="on"></i><i class="on"></i><i></i><i></i><i></i><i></i><i></i><i></i><i></i><i></i><i></i><i></i><i></i></span>
  </div>
  <div class="progress">
    <span class="progress__pct">10%</span>
    <div class="progress__track"><div class="progress__fill"></div></div>
    <span class="progress__lesson">Lesson 2</span>
    <span class="progress__prev"><svg width="11" height="7" viewBox="0 0 11 7"><path d="M10.5 3.5H1M4 .5L1 3.5 4 6.5" fill="none" stroke="#5cc443" stroke-width="1.2"/></svg>Prev.</span>
    <span class="progress__next">Next<svg width="11" height="7" viewBox="0 0 11 7"><path d="M.5 3.5H10M7 .5l3 3-3 3" fill="none" stroke="#5cc443" stroke-width="1.2"/></svg></span>
  </div>
</section>

<section class="slide slide--gallery">
  <header class="topbar">
    <div class="brand"><i class="brand__mark"></i>Company name</div>
    <nav class="nav"><span>Lessons</span><span>Menu</span><span>Glossary</span></nav>
  </header>
  <p class="kicker">Handling sensitive information</p>
  <h2 class="headline">Blandit preasent luptatum zzril delenit augue duis dolore</h2>
  <svg width="0" height="0" style="position:absolute">
    <defs>
      <symbol id="placeholder" viewBox="0 0 83 50">
        <rect x=".5" y=".5" width="82" height="49" rx="2" fill="#f3f3f5" stroke="#d9dadf"/>
        <circle cx="23" cy="19" r="7" fill="#e4e5e9"/>
        <path d="M1 49L30 26l18 15 14-11 20 16v3z" fill="#e4e5e9"/>
      </symbol>
    </defs>
  </svg>
  <div class="grid">
    <div class="tile" style="left:0;top:0"><svg><use href="#placeholder"/></svg><span>Lorem ipsum</span></div>
    <div class="tile" style="left:98px;top:0"><svg><use href="#placeholder"/></svg><span>Lorem ipsum</span></div>
    <div class="tile" style="left:196px;top:0"><svg><use href="#placeholder"/></svg></div>
    <div class="tile" style="left:295px;top:0"><svg><use href="#placeholder"/></svg><span>Lorem ipsum</span></div>
    <div class="tile" style="left:0;top:73px"><svg><use href="#placeholder"/></svg><span>Lorem ipsum</span></div>
    <div class="tile" style="left:98px;top:73px"><svg><use href="#placeholder"/></svg><span>Lorem ipsum</span></div>
    <div class="tile" style="left:196px;top:73px"><svg><use href="#placeholder"/></svg><span>Lorem ipsum</span></div>
    <div class="tile" style="left:295px;top:73px"><svg><use href="#placeholder"/></svg><span>Lorem ipsum</span></div>
  </div>
  <div class="tip">Consectetur adipiscing elit, sed do eiusmod tempor incididunt ut labore et dolore magna.</div>
  <div class="progress">
    <span class="progress__pct">10%</span>
    <div class="progress__track"><div class="progress__fill"></div></div>
    <span class="progress__lesson">Lesson 2</span>
    <span class="progress__prev"><svg width="11" height="7" viewBox="0 0 11 7"><path d="M10.5 3.5H1M4 .5L1 3.5 4 6.5" fill="none" stroke="#5cc443" stroke-width="1.2"/></svg>Prev.</span>
    <span class="progress__next">Next<svg width="11" height="7" viewBox="0 0 11 7"><path d="M.5 3.5H10M7 .5l3 3-3 3" fill="none" stroke="#5cc443" stroke-width="1.2"/></svg></span>
  </div>
</section>

</body>
</html>
```